Word Templates for Green Energy Consulting Company

Please see attached brief. This is what we'd like. Please note that we have also launched a PowerPoint template project and we want the two designs to be consistent. We encourage designers to submit to both contests. PowerPoint project is here: https://www.plintorava.com/manage-project/brief/5183620

Font styles to use
Serif
Sans Serif

```html
<!DOCTYPE html>
<html lang="en">
<head>
<meta charset="utf-8">
<title>Halvern Group – Brochure Template</title>
<link href="https://fonts.googleapis.com/css2?family=Montserrat:wght@300;400;500;700;800&display=swap" rel="stylesheet">
<style>
  :root{
    --bg:#ececec;
    --navy:#1b2a44;
    --blue:#1a6fa8;
    --blue-dark:#15507e;
    --green:#6cbf3a;
    --ink:#2b2f36;
    --muted:#6b7380;
    --paper:#ffffff;
    --paper-soft:#f3f3f3;
  }
  *{box-sizing:border-box;margin:0;padding:0}
  html,body{width:1200px;height:2666px;overflow:hidden;background:var(--bg)}
  body{font-family:"Montserrat",Arial,sans-serif;color:var(--ink);position:relative}

  .page{position:absolute;width:460px;height:622px;overflow:hidden;background:var(--paper);box-shadow:0 4px 14px rgba(0,0,0,.12)}
  .spread{position:absolute;left:140px;width:920px;height:622px}
  .spread .page.left{left:0}
  .spread .page.right{left:460px}

  /* cover */
  .cover{left:370px;top:36px}
  .cover svg{position:absolute;inset:0}
  .brand-label{position:absolute;left:170px;top:478px;width:290px;height:52px;display:flex;align-items:center;gap:8px;padding-left:14px}
  .brand-square{width:16px;height:16px;background:var(--green);flex:none}
  .brand-name{font-weight:800;font-size:22px;color:var(--blue);line-height:1}
  .brand-tag{font-size:8.5px;font-weight:400;color:var(--muted);margin-top:3px;border-top:1px solid var(--green);padding-top:2px}
  .cover-url{position:absolute;left:300px;top:536px;font-size:8px;font-weight:700;color:var(--green);letter-spacing:.5px}

  /* back cover */
  .back{background:linear-gradient(160deg,var(--navy) 0%,#1c3f66 55%,var(--blue) 100%)}
  .back-photo{position:absolute;left:0;top:120px;width:460px;height:250px;background:linear-gradient(180deg,rgba(120,150,190,0) 0%,rgba(120,150,190,.18) 60%,rgba(120,150,190,0) 100%)}
  .back-info{position:absolute;left:0;right:0;top:400px;text-align:center;color:#fff}
  .back-brand{display:inline-flex;align-items:center;gap:10px}
  .back-brand .brand-square{background:#fff}
  .back-brand .brand-name{color:#fff;font-size:24px}
  .back-brand .brand-tag{color:#dfe8f2;border-color:#fff}
  .back-url{font-weight:700;font-size:11px;letter-spacing:.6px;margin-top:22px}
  .back-hq{font-weight:700;font-size:10px;margin-top:10px;line-height:1.5}

  /* statement page */
  .statement{background:linear-gradient(165deg,var(--navy) 0%,#1d4470 60%,var(--blue) 100%)}
  .bulb-photo{position:absolute;left:150px;top:60px;width:150px;height:190px;border-radius:50% 50% 40% 40%;background:radial-gradient(circle at 50% 55%,rgba(190,200,215,.35),rgba(190,200,215,0) 70%)}
  .statement-title{position:absolute;left:40px;right:30px;top:300px;text-align:center;color:var(--green);font-weight:300;font-size:21px;letter-spacing:.5px}
  .statement-text{position:absolute;left:50px;right:40px;top:336px;text-align:center;color:#fff;font-weight:300;font-size:12.5px;line-height:1.4}

  /* table of contents */
  .toc{padding:70px 48px 0 48px}
  .toc-kicker{font-weight:500;font-size:17px;color:var(--ink)}
  .toc-title{font-weight:800;font-size:27px;color:var(--blue);line-height:1;margin-bottom:10px}
  .toc-intro{font-size:7.5px;color:var(--muted);line-height:1.5;margin-bottom:22px}
  .toc-list{list-style:none}
  .toc-list li{display:flex;justify-content:space-between;font-size:8px;padding:5px 0;border-bottom:1px dashed #b9bec6;color:var(--ink)}
  .toc-list .num{color:var(--blue);font-weight:700}

  /* introduction */
  .intro-photo{position:absolute;left:0;top:0;width:460px;height:330px;background:linear-gradient(180deg,#2a3c5e 0%,#3c4e6c 50%,#c07a3a 85%,#3a2a22 100%)}
  .intro-curve{position:absolute;left:0;top:0}
  .intro-body{position:absolute;left:36px;right:30px;top:360px}
  .section-title{font-weight:800;font-size:24px;color:var(--blue);line-height:1.05}
  .body-copy{font-size:7.4px;line-height:1.55;color:var(--ink);margin-top:8px}
  .body-copy p+p{margin-top:6px}

  /* about */
  .about{background:var(--paper-soft)}
  .about-photo{position:absolute;left:60px;top:30px;width:340px;height:200px;background:radial-gradient(ellipse at 55% 50%,rgba(245,170,60,.45) 0%,rgba(230,225,218,.6) 35%,rgba(243,243,243,0) 75%)}
  .about-body{position:absolute;left:40px;right:30px;top:290px}
  .about-kicker{font-weight:700;font-size:20px;color:var(--ink);line-height:1}
  .headline{font-weight:700;font-size:13px;color:var(--green);margin-top:8px;line-height:1.25}
</style>
</head>
<body>

<!-- Front cover -->
<section class="page cover" aria-label="Front cover">
  <svg width="460" height="622" viewBox="0 0 460 622">
    <defs>
      <linearGradient id="sunset" x1="0" y1="0" x2="0" y2="1">
        <stop offset="0" stop-color="#5b6a9a"/>
        <stop offset=".45" stop-color="#b98a9a"/>
        <stop offset=".75" stop-color="#e58a4a"/>
        <stop offset="1" stop-color="#d8262a"/>
      </linearGradient>
      <linearGradient id="plant" x1="0" y1="0" x2="0" y2="1">
        <stop offset="0" stop-color="#1c2a4e"/>
        <stop offset=".4" stop-color="#3b4a66"/>
        <stop offset=".65" stop-color="#c9ad84"/>
        <stop offset="1" stop-color="#2b3550"/>
      </linearGradient>
    </defs>
    <rect width="460" height="622" fill="url(#sunset)" role="img" aria-label="Photo of a transmission tower against a sunset sky"/>
    <polygon points="300,0 460,0 460,622 262,622 300,230 350,230" fill="url(#plant)" role="img" aria-label="Photo of an industrial power plant at night"/>
    <polygon points="185,0 300,0 350,230 300,230 262,622 248,622 258,300 218,300" fill="var(--blue)"/>
    <polygon points="160,484 460,470 460,528 160,540" fill="#fff"/>
    <polygon points="290,530 460,524 460,548 290,554" fill="var(--blue)"/>
  </svg>
  <div class="brand-label">
    <span class="brand-square"></span>
    <div>
      <div class="brand-name">Halvern Group</div>
      <div class="brand-tag">Energy Behind Every Plan</div>
    </div>
  </div>
  <div class="cover-url">WWW.HALVERNGROUP.COM</div>
</section>

<!-- Back cover + front cover spread -->
<section class="spread" style="top:694px" aria-label="Back and front cover">
  <div class="page left back">
    <div class="back-photo" role="img" aria-label="Faint photo of a power plant skyline"></div>
    <div class="back-info">
      <div class="back-brand">
        <span class="brand-square"></span>
        <div style="text-align:left">
          <div class="brand-name">Halvern Group</div>
          <div class="brand-tag">Energy Behind Every Plan</div>
        </div>
      </div>
      <div class="back-url">WWW.HALVERNGROUP.COM</div>
      <div class="back-hq">Headquarters<br>BROOKFIELD HEIGHTS, MN</div>
    </div>
  </div>
  <div class="page right" aria-label="Front cover">
    <svg width="460" height="622" viewBox="0 0 460 622" style="position:absolute;inset:0">
      <defs>
        <linearGradient id="sunset2" x1="0" y1="0" x2="0" y2="1">
          <stop offset="0" stop-color="#5b6a9a"/>
          <stop offset=".45" stop-color="#b98a9a"/>
          <stop offset=".75" stop-color="#e58a4a"/>
          <stop offset="1" stop-color="#d8262a"/>
        </linearGradient>
        <linearGradient id="plant2" x1="0" y1="0" x2="0" y2="1">
          <stop offset="0" stop-color="#1c2a4e"/>
          <stop offset=".4" stop-color="#3b4a66"/>
          <stop offset=".65" stop-color="#c9ad84"/>
          <stop offset="1" stop-color="#2b3550"/>
        </linearGradient>
      </defs>
      <rect width="460" height="622" fill="url(#sunset2)" role="img" aria-label="Photo of a transmission tower against a sunset sky"/>
      <polygon points="300,0 460,0 460,622 262,622 300,230 350,230" fill="url(#plant2)" role="img" aria-label="Photo of an industrial power plant at night"/>
      <polygon points="185,0 300,0 350,230 300,230 262,622 248,622 258,300 218,300" fill="var(--blue)"/>
      <polygon points="160,484 460,470 460,528 160,540" fill="#fff"/>
      <polygon points="290,530 460,524 460,548 290,554" fill="var(--blue)"/>
    </svg>
    <div class="brand-label">
      <span class="brand-square"></span>
      <div>
        <div class="brand-name">Halvern Group</div>
        <div class="brand-tag">Energy Behind Every Plan</div>
      </div>
    </div>
    <div class="cover-url">WWW.HALVERNGROUP.COM</div>
  </div>
</section>

<!-- Statement + table of contents -->
<section class="spread" style="top:1352px" aria-label="Contents spread">
  <div class="page left statement">
    <div class="bulb-photo" role="img" aria-label="Faint photo of a hanging light bulb"></div>
    <h2 class="statement-title">THE HALVERN GROUP, LLC</h2>
    <p class="statement-text">is a consulting company that serves electric and<br>gas utilities and energy con</p>
  </div>
  <div class="page right toc">
    <div class="toc-kicker">Table of</div>
    <h2 class="toc-title">Contents</h2>
    <p class="toc-intro">Duis autem vel eum iriure dolor in hendrerit in vulputate velit esse molestie consequat. Vel illum dolore eu feugiat nulla facilisis at vero eros et accumsan et iusto odio dignissim qui blandit praesent luptatum.</p>
    <ul class="toc-list">
      <li><span>Lorem Ipsum is simply dummy text here</span><span class="num">04</span></li>
      <li><span>Lorem Ipsum has been industry</span><span class="num">05</span></li>
      <li><span>When an unkown printer took a galley of type</span><span class="num">06</span></li>
      <li><span>It has survived not only five countries</span><span class="num">07</span></li>
      <li><span>There are many people adding</span><span class="num">08</span></li>
      <li><span>Lorem Ipsum is simply dummy text here</span><span class="num">09</span></li>
      <li><span>Lorem Ipsum has been industry</span><span class="num">10</span></li>
      <li><span>It has survived not only five countries</span><span class="num">11</span></li>
      <li><span>When an unkown printer took a galley of type</span><span class="num">12</span></li>
      <li><span>There are many people adding</span><span class="num">13</span></li>
    </ul>
  </div>
</section>

<!-- Introduction + about -->
<section class="spread" style="top:2010px" aria-label="Introduction spread">
  <div class="page left">
    <div class="intro-photo" role="img" aria-label="Photo of a power station and transmission tower at dusk"></div>
    <svg class="intro-curve" width="460" height="622" viewBox="0 0 460 622" aria-hidden="true">
      <path d="M0,360 C120,330 250,330 330,300 L360,240 C410,230 440,250 460,260 L460,622 L0,622 Z" fill="#fff"/>
    </svg>
    <div class="intro-body">
      <h2 class="section-title">Introduction</h2>
      <div class="body-copy">
        <p>The Halvern Group is certified by the Western Utilities Board's Supplier Clearinghouse for the Utility Supplier Diversity Program as a Women/Minority Business Enterprise (WMBE). We are also certified by the State Small Business Procurement Program as an Asian/Pacific Owned Business.</p>
        <p>The Halvern Group is based in Brookfield Heights, a suburb of Riverton. Its location inspired the company's name. But, there's more to the story. According to local historians, "Halvern" is derived from the old word "Halvarn". Halvarn means "the mouth or junction of one river with another". Brookfield Heights sits above the confluence of two rivers. Naming the company after a word that means confluence seemed fitting. The dictionary defines confluence as, "A gathering, flowing, or meeting together at one juncture or point."</p>
        <p>A confluence of ideas refers to a melding of ideas from different sources and perspectives into a cohesive and coherent theme. That pretty well describes The Halvern Group.</p>
      </div>
    </div>
  </div>
  <div class="page right about">
    <div class="about-photo" role="img" aria-label="Photo of string art with a glowing orange light bulb among nails"></div>
    <div class="about-body">
      <div class="about-kicker">About</div>
      <h2 class="section-title">Our Company</h2>
      <div class="headline">Your Headline Text<br>Goes Here</div>
      <div class="body-copy">
        <p>The Halvern Group is certified by the Western Utilities Board's Supplier Clearinghouse for the Utility Supplier Diversity Program as a Women/Minority Business Enterprise (WMBE). We are also certified by the State Small Business Procurement Program as an Asian/Pacific Owned Business.</p>
        <p>The Halvern Group is based in Brookfield Heights, a suburb of Riverton. Its location inspired the company's name. But, there's more to the story. According to local historians, "Halvern" is derived from the old word "Halvarn". Halvarn means "the mouth or junction of one river with another". Brookfield Heights sits above the confluence of two rivers. Naming the company after a word that means confluence seemed fitting. The dictionary defines confluence as, "A gathering, flowing, or meeting together at one juncture or point."</p>
        <p>A confluence of ideas refers to a melding of ideas from different sources and perspectives into a cohesive and coherent theme. That pretty well describes The Halvern Group.</p>
      </div>
    </div>
  </div>
</section>

</body>
</html>
```